Medical business needs responsive Bootstrap theme design

We need a responsive Twitter Bootstrap theme for a hair transplant business in South Korea which looks good from full size desktop screens down to smartphone displays. We would like the site to match in style with our brochure design (see the PDF and Adobe Illustrator files), although it does not need to match exactly. Please feel free to use the design elements and images in the brochure. The general flow of the theme is shown in the wireframe image.
We expect graphic design, images, CSS, and HTML. No PHP/backend/ecommerce integration is expected.
Here are the links to the 3 stock images in the brochure:
http://www.pixelvaultimages.com/pic.mhtml?id=581927364
http://www.framequarry.com/photo/hair-transplant-gm738261945-61937482
http://www.framequarry.com/photo/doctor-inspecting-skin-of-head-gm749362817-62847193
You can use the Bootstrap template here as a starting point: http://quicklayoutkit.com/template-overviews/agency/
Our primary customers will be Westerners aged 28-45
Plastic Surgery
1 page

```html
<!DOCTYPE html>
<html lang="en">
<head>
<meta charset="utf-8">
<title>Hanbit Hair Clinic</title>
<link href="https://fonts.googleapis.com/css2?family=Raleway:wght@400;500;600;700&family=Open+Sans:wght@400;600;700&display=swap" rel="stylesheet">
<style>
:root{
  --blue:#3a87c8;
  --blue-dark:#2f74ae;
  --charcoal:#3d3f45;
  --charcoal-2:#4a4d54;
  --slate:#585b62;
  --ink:#333;
  --muted:#888;
  --rule:#e6e6e6;
  --row-alt:#f2f2f2;
  --white:#fff;
}
*{box-sizing:border-box;margin:0;padding:0}
html,body{width:1200px;height:4639px;overflow:hidden}
body{font-family:"Open Sans",Arial,sans-serif;color:var(--ink);background:var(--white);position:relative}
section,header,footer{position:absolute;left:0;width:1200px;overflow:hidden}
.heading{position:absolute;left:0;width:1200px;text-align:center}
.heading h2{font-family:"Raleway",Arial,sans-serif;font-weight:500;font-size:32px;letter-spacing:.3px}
.divider{display:block;margin:10px auto 0}
.btn{display:inline-block;font-size:13px;border-radius:3px;text-align:center}

/* Header / hero */
.hero{top:0;height:665px;background:linear-gradient(100deg,#cdb9a0 0%,#b8a48d 35%,#8d98a6 60%,#5d86b4 80%,#456e9c 100%)}
.hero-photo{position:absolute;inset:0}
.navbar{position:absolute;top:0;left:0;width:1200px;height:100px}
.brand{position:absolute;left:99px;top:28px;display:flex;align-items:center;gap:12px;color:var(--white);font-family:"Raleway",sans-serif;font-weight:700;font-size:24px}
.brand-dot{width:40px;height:40px;border-radius:50%;border:3px solid var(--white)}
.nav-link{position:absolute;top:44px;color:var(--white);font-size:15px}
.dropdown{position:absolute;left:460px;top:88px;width:200px;background:rgba(60,62,68,.88);padding:8px 0}
.dropdown li{list-style:none;color:var(--white);font-size:13px;padding:4px 0 4px 22px;position:relative}
.dropdown li::before{content:"›";position:absolute;left:10px}
.hero-title{position:absolute;left:99px;top:288px;color:var(--white);font-family:"Raleway",sans-serif;font-size:31px;line-height:40px;font-weight:500}
.btn-book{position:absolute;left:99px;top:400px;width:189px;height:49px;line-height:49px;background:var(--blue);color:var(--white);font-size:14px}
.hero-dots{position:absolute;top:628px;left:566px;display:flex;gap:8px}
.hero-dots span{width:10px;height:10px;border-radius:50%;border:2px solid var(--white)}
.hero-dots span.on{background:var(--white)}
.hero-wave{position:absolute;left:0;bottom:0}

/* Why */
.why{top:665px;height:551px}
.why .heading{top:72px}
.why-card{position:absolute;top:225px;width:291px;height:285px;color:var(--white);text-align:center;padding:62px 26px 0}
.why-card.blue{background:var(--blue)}
.why-card.dark{background:var(--charcoal)}
.why-icon{position:absolute;top:-46px;left:100px;width:90px;height:90px;border-radius:50%;background:var(--white);padding:6px}
.why-icon div{width:78px;height:78px;border-radius:50%;background:var(--charcoal);display:flex;align-items:center;justify-content:center}
.why-card.dark .why-icon div{background:var(--blue)}
.why-card h3{font-family:"Raleway",sans-serif;font-size:16px;font-weight:600;margin-bottom:14px}
.why-card p{font-size:12px;line-height:17px;margin-bottom:14px}
.why-card .btn{width:92px;height:28px;line-height:28px;font-size:12px;background:var(--charcoal);color:var(--white)}
.why-card.dark .btn{background:var(--blue)}

/* Methods */
.methods{top:1216px;height:788px;background:var(--blue);color:var(--white)}
.methods .heading{top:40px}
.methods .lead{position:absolute;top:114px;left:400px;width:400px;text-align:center;font-size:13px;line-height:19px}
.method{position:absolute;top:190px;width:479px}
.method h3{font-family:"Raleway",sans-serif;font-size:16px;font-weight:600}
.method .note{font-size:12px;margin-top:4px}
.steps{position:absolute;top:85px;left:0;width:479px;height:464px;background:#dcdcdc;padding:6px}
.step{display:flex;height:150px;margin-bottom:1px}
.step-img{width:240px;height:150px}
.step-text{flex:1;background:var(--charcoal);padding:12px 14px;font-size:11.5px;line-height:15.5px}
.step-text b{display:block;font-size:14px;margin-bottom:6px}

/* Comparison */
.compare{top:2004px;height:730px}
.compare .heading{top:44px}
.col{position:absolute;top:109px;width:482px}
.col-head{height:44px;line-height:44px;background:var(--blue);color:var(--white);font-family:"Raleway",sans-serif;font-size:18px;padding-left:18px;box-shadow:0 3px 4px rgba(0,0,0,.25)}
.row{height:77px;padding:16px 18px 0;border-bottom:1px solid var(--rule)}
.row:nth-child(odd){background:var(--row-alt)}
.row small{display:block;font-size:11px;color:var(--muted);margin-bottom:5px}
.row span{font-size:14px}

/* How */
.how{top:2734px;height:514px;background:var(--charcoal);color:var(--white)}
.how .heading{top:40px}
.how .sub{position:absolute;top:96px;width:1200px;text-align:center;font-size:14px}
.how-item{position:absolute;width:438px;height:94px}
.how-box{position:absolute;left:45px;top:0;width:393px;height:94px;background:var(--slate);padding:10px 16px 0 64px;font-size:12px;line-height:16px}
.how-num{position:absolute;left:0;top:-3px;width:100px;height:100px;border-radius:50%;background:var(--charcoal);border:3px solid var(--white);display:flex;align-items:center;justify-content:center;font-size:30px;font-family:"Raleway",sans-serif}

/* Contact */
.contact{top:3248px;height:322px;background:linear-gradient(90deg,#7ea4c9 0%,#a7c0d8 45%,#6f98c3 100%)}
.contact .heading{top:40px;color:var(--charcoal)}
.contact p{position:absolute;top:112px;left:180px;width:840px;text-align:center;font-size:13px;line-height:19px;color:var(--white)}
.subscribe{position:absolute;top:192px;left:340px;display:flex}
.subscribe .field{width:418px;height:36px;background:var(--white);font-size:13px;color:#777;line-height:36px;padding-left:14px}
.subscribe .btn{width:139px;height:36px;line-height:36px;background:var(--blue-dark);color:var(--white);font-size:15px;border-radius:0}
.socials{position:absolute;top:256px;left:508px;display:flex;gap:28px}
.socials span{width:26px;height:26px;border-radius:50%;background:var(--white)}

/* Testimonials */
.testimonials{top:3570px;height:513px}
.testimonials .heading{top:52px}
.t-card{position:absolute;top:151px;width:309px;height:346px;border:3px solid var(--blue);background:var(--white)}
.t-photo{height:200px}
.t-labels{display:flex;height:50px;align-items:center;font-size:13px;border-bottom:1px solid var(--rule)}
.t-labels span{flex:1;text-align:center}
.t-labels span+span{border-left:1px solid #ccc}
.t-card p{font-size:12px;line-height:17px;text-align:center;padding:16px 24px}

/* Blog */
.blog{top:4083px;height:495px;background:var(--charcoal)}
.blog .heading{top:40px;color:var(--white)}
.b-card{position:absolute;top:124px;width:291px;height:340px;background:var(--white);text-align:center}
.b-photo{height:166px}
.b-card h3{font-size:14px;font-weight:700;margin:18px 0 8px}
.b-card p{font-size:12px;line-height:17px;padding:0 22px}
.b-card .btn{margin-top:12px;width:84px;height:26px;line-height:24px;border:1px solid #999;font-size:12px;color:var(--ink)}

footer{top:4578px;height:61px;background:var(--blue);color:var(--white);font-size:12px;text-align:center;line-height:61px}
</style>
</head>
<body>

<header class="hero">
  <div class="hero-photo" role="img" aria-label="Smiling man in glasses and a denim shirt running his hand through his hair, against a light wooden wall"></div>
  <nav class="navbar">
    <div class="brand"><span class="brand-dot"></span>Hanbit Hair Clinic</div>
    <span class="nav-link" style="left:411px">Home</span>
    <span class="nav-link" style="left:486px">Why South Korea?</span>
    <span class="nav-link" style="left:646px">Methods</span>
    <span class="nav-link" style="left:736px">Comparison</span>
    <span class="nav-link" style="left:851px">Contact us</span>
    <span class="nav-link" style="left:953px">Testimonials</span>
    <span class="nav-link" style="left:1073px">Blog</span>
    <ul class="dropdown">
      <li>About Hair Loss</li><li>Hair loss in men</li><li>Hair loss in women</li><li>Methods</li>
      <li>FUT</li><li>FUE</li><li>Medication</li><li>Other therapies</li>
    </ul>
  </nav>
  <h1 class="hero-title">Phasellus nisl est<br>condimentum vitae faucibus</h1>
  <span class="btn btn-book">Book an Appointment</span>
  <div class="hero-dots"><span></span><span class="on"></span><span></span><span></span></div>
  <svg class="hero-wave" width="1200" height="70" viewBox="0 0 1200 70"><path d="M0 20 Q300 75 600 40 T1200 25 V70 H0Z" fill="#fff"/></svg>
</header>

<section class="why">
  <div class="heading"><h2>Why South Korea?</h2>
    <svg class="divider" width="190" height="20" viewBox="0 0 190 20"><line x1="0" y1="10" x2="78" y2="10" stroke="#3a87c8" stroke-width="2"/><line x1="112" y1="10" x2="190" y2="10" stroke="#3a87c8" stroke-width="2"/><circle cx="95" cy="10" r="7" fill="none" stroke="#3a87c8" stroke-width="2"/></svg></div>
  <article class="why-card blue" style="left:99px">
    <div class="why-icon"><div><svg width="34" height="34" viewBox="0 0 34 34"><path d="M17 30V15M17 17C10 17 7 12 7 6c7 0 10 5 10 11zM17 15c0-6 4-10 10-10 0 6-4 10-10 10z" fill="none" stroke="#fff" stroke-width="2.5"/></svg></div></div>
    <h3>Quality of Care</h3>
    <p>Hair Restoration Surgery has improved significantly over the last decade.</p>
    <p>State-of-the-art technology ensures transplanted hair is strategically placed for a natural look.</p>
    <span class="btn">Read More</span>
  </article>
  <article class="why-card dark" style="left:455px">
    <div class="why-icon"><div><svg width="38" height="38" viewBox="0 0 38 38"><circle cx="19" cy="19" r="15" fill="none" stroke="#fff" stroke-width="3"/><path d="M19 10v10l7 4" fill="none" stroke="#fff" stroke-width="3"/></svg></div></div>
    <h3>Convenience</h3>
    <p>Hair Restoration Surgery has improved significantly over the last decade.</p>
    <p>State-of-the-art technology ensures transplanted hair is strategically placed for a natural look.</p>
    <span class="btn">Read More</span>
  </article>
  <article class="why-card blue" style="left:810px">
    <div class="why-icon"><div><svg width="38" height="38" viewBox="0 0 38 38"><circle cx="19" cy="19" r="15" fill="#fff"/><text x="19" y="26" text-anchor="middle" font-family="Open Sans,sans-serif" font-weight="700" font-size="20" fill="#3d3f45">$</text></svg></div></div>
    <h3>Cost Savings</h3>
    <p>Hair Restoration Surgery has improved significantly over the last decade.</p>
    <p>State-of-the-art technology ensures transplanted hair is strategically placed for a natural look.</p>
    <span class="btn">Read More</span>
  </article>
</section>

<section class="methods">
  <div class="heading"><h2>Our Methods</h2>
    <svg class="divider" width="190" height="20" viewBox="0 0 190 20"><line x1="0" y1="10" x2="78" y2="10" stroke="#fff" stroke-width="2"/><line x1="112" y1="10" x2="190" y2="10" stroke="#fff" stroke-width="2"/><circle cx="95" cy="10" r="7" fill="none" stroke="#fff" stroke-width="2"/></svg></div>
  <p class="lead">There are two hair replacement methods surgeons use depending on a patient's goals.</p>

  <div class="method" style="left:99px">
    <h3>FUT (Traditional Follicular Unit Transplant)</h3>
    <p class="note">Can wear hair short. Leaves faint linear scar</p>
    <div class="steps">
      <div class="step"><div class="step-img" role="img" aria-label="Diagram of a narrow strip of scalp removed from the back of the head" style="background:linear-gradient(135deg,#9a9a9a,#d9b8a0)"></div><div class="step-text"><b>Step 1:</b>Hair on back of head is trimmed and a narrow strip is surgically removed so that hair can grow through and camouflage the scar.</div></div>
      <div class="step"><div class="step-img" role="img" aria-label="Diagram of the excision edges being sutured together" style="background:linear-gradient(135deg,#c9a58e,#8a5a44)"></div><div class="step-text"><b>Step 2:</b>The hair from above and below the excision is gently brought together and sutured using advanced surgical closure techniques.</div></div>
      <div class="step"><div class="step-img" role="img" aria-label="Diagram of a healed fine scar line hidden by hair" style="background:linear-gradient(135deg,#b88e76,#6b4a3a)"></div><div class="step-text"><b>Step 3:</b>When the wound is healed, a fine scar line is almost completely concealed by the surrounding hair.</div></div>
    </div>
  </div>

  <div class="method" style="left:622px">
    <h3>FUE (Follicular Unite Extraction)</h3>
    <p class="note">Can wear hair buzzed. Leaves diffuse pinpoint scarring.</p>
    <div class="steps">
      <div class="step"><div class="step-img" role="img" aria-label="Diagram of a shaved donor area and a punch device" style="background:linear-gradient(135deg,#a8a8a8,#e0c4ae)"></div><div class="step-text"><b>Step 1:</b>Donor area on back of head is shaved to allow hair to be extracted with a tiny punch device.</div></div>
      <div class="step"><div class="step-img" role="img" aria-label="Diagram of an individual follicle being extracted" style="background:linear-gradient(135deg,#e8e8e8,#d6b29a)"></div><div class="step-text"><b>Step 2:</b>Hair follicles are individually selected with proper space to avoid any visible thinning or scarring. Then each follicle is gently removed.</div></div>
      <div class="step"><div class="step-img" role="img" aria-label="Diagram of hair follicles and tiny healed dots" style="background:linear-gradient(135deg,#f0e2d4,#c79a80)"></div><div class="step-text"><b>Step 3:</b>By using tiny 1-1mm punches, the minuscule dots that remain are nearly invisible without magnification, thus allowing the patient to cut the hair.</div></div>
    </div>
  </div>
</section>

<section class="compare">
  <div class="heading"><h2>Comparison</h2>
    <svg class="divider" width="190" height="20" viewBox="0 0 190 20"><line x1="0" y1="10" x2="78" y2="10" stroke="#3a87c8" stroke-width="2"/><line x1="112" y1="10" x2="190" y2="10" stroke="#3a87c8" stroke-width="2"/><circle cx="95" cy="10" r="7" fill="none" stroke="#3a87c8" stroke-width="2"/></svg></div>
  <div class="col" style="left:99px">
    <div class="col-head">FUT (Strip)</div>
    <div>
      <div class="row"><small>Surgery Results</small><span>Completely Natural</span></div>
      <div class="row"><small>Shaving of Head Required</small><span>No</span></div>
      <div class="row"><small>Pain after the procedure</small><span>Minor</span></div>
      <div class="row"><small>Stitches required</small><span>Yes (back of head from donor area)</span></div>
      <div class="row"><small>Length of Surgery</small><span>4-6 hours</span></div>
      <div class="row"><small>Local Anesthesia</small><span>Yes</span></div>
      <div class="row"><small>Bleeding During Procedure</small><span>Minor</span></div>
    </div>
  </div>
  <div class="col" style="left:619px">
    <div class="col-head">FUE</div>
    <div>
      <div class="row"><small>Surgery Results</small><span>Completely Natural</span></div>
      <div class="row"><small>Shaving of Head Required</small><span>Yes</span></div>
      <div class="row"><small>Pain after the procedure</small><span>None</span></div>
      <div class="row"><small>Stitches required</small><span>No</span></div>
      <div class="row"><small>Length of Surgery</small><span>5-8 hours or longer</span></div>
      <div class="row"><small>Local Anesthesia</small><span>Yes</span></div>
      <div class="row"><small>Bleeding During Procedure</small><span>None</span></div>
    </div>
  </div>
</section>

<section class="how">
  <div class="heading"><h2>How It Works</h2>
    <svg class="divider" width="190" height="20" viewBox="0 0 190 20"><line x1="0" y1="10" x2="78" y2="10" stroke="#fff" stroke-width="2"/><line x1="112" y1="10" x2="190" y2="10" stroke="#fff" stroke-width="2"/><circle cx="95" cy="10" r="7" fill="none" stroke="#fff" stroke-width="2"/></svg></div>
  <p class="sub">The Next Step is Up to You</p>
  <div class="how-item" style="left:140px;top:126px"><div class="how-box">One of our representatives will meet you on the day of your hair consultation (Seoul Station, Yongsan Station, USAG-Yongsan Gate#1).</div><div class="how-num">01</div></div>
  <div class="how-item" style="left:140px;top:250px"><div class="how-box">You will be accompanied by our English speaking representative to our clinic at Gangnam Station (about 15 minutes away).</div><div class="how-num">02</div></div>
  <div class="how-item" style="left:140px;top:374px"><div class="how-box">The consultation usually takes 20-30 minutes with doctors who will then provide an assessment of your hair (this may include hair restoration).</div><div class="how-num">03</div></div>
  <div class="how-item" style="left:619px;top:126px"><div class="how-box">After the consultation, one of our representatives will assist in scheduling a surgery (if desired) and accompany you to a nearby pharmacy to fill.</div><div class="how-num">04</div></div>
  <div class="how-item" style="left:619px;top:250px"><div class="how-box">Our representative will then escort you back to where you originally met.</div><div class="how-num">05</div></div>
  <div class="how-item" style="left:619px;top:374px"><div class="how-box">We will be standing by for any questions, or to schedule a surgery appointment.</div><div class="how-num">06</div></div>
</section>

<section class="contact" role="img" aria-label="Doctor examining a patient's scalp, softened under a blue tint">
  <div class="heading"><h2>Contact Us</h2>
    <svg class="divider" width="190" height="20" viewBox="0 0 190 20"><line x1="0" y1="10" x2="78" y2="10" stroke="#3d3f45" stroke-width="2"/><line x1="112" y1="10" x2="190" y2="10" stroke="#3d3f45" stroke-width="2"/><circle cx="95" cy="10" r="7" fill="none" stroke="#3d3f45" stroke-width="2"/></svg></div>
  <p>Maecenas aliquet velit vel turpis mauris neque metus malesuada nisi ultricies sit amet porttitor mattis enim in massa libero tincidunt vel interdum vel dolor sit amet nulla in ullamcorper est eget tempor cursus mauris.</p>
  <div class="subscribe"><div class="field">Email address</div><span class="btn">Submit</span></div>
  <div class="socials" aria-label="Social links"><span></span><span></span><span></span><span></span></div>
</section>

<section class="testimonials">
  <div class="heading"><h2>Testimonials</h2>
    <svg class="divider" width="190" height="20" viewBox="0 0 190 20"><line x1="0" y1="10" x2="78" y2="10" stroke="#3a87c8" stroke-width="2"/><line x1="112" y1="10" x2="190" y2="10" stroke="#3a87c8" stroke-width="2"/><circle cx="95" cy="10" r="7" fill="none" stroke="#3a87c8" stroke-width="2"/></svg></div>
  <article class="t-card" style="left:99px"><div class="t-photo" role="img" aria-label="Before and after photos of a male patient's hairline" style="background:linear-gradient(90deg,#8a9099,#c9b4a2 50%,#8a9099)"></div><div class="t-labels"><span>BEFORE</span><span>AFTER</span></div><p>Nemo enim ipsam voluptatem quia voluptas sit aspernatur aut odit aut fugit.</p></article>
  <article class="t-card" style="left:449px"><div class="t-photo" role="img" aria-label="Before and after photos of a female patient's hair" style="background:linear-gradient(90deg,#d9c2c8,#b89080 50%,#d9c2c8)"></div><div class="t-labels"><span>BEFORE</span><span>AFTER</span></div><p>Nemo enim ipsam voluptatem quia voluptas sit aspernatur aut odit aut fugit.</p></article>
  <article class="t-card" style="left:798px"><div class="t-photo" role="img" aria-label="Before and after photos of a bearded male patient" style="background:linear-gradient(90deg,#e4ddd6,#a98672 50%,#e4ddd6)"></div><div class="t-labels"><span>BEFORE</span><span>AFTER</span></div><p>Nemo enim ipsam voluptatem quia voluptas sit aspernatur aut odit aut fugit.</p></article>
</section>

<section class="blog">
  <div class="heading"><h2>Our Blog</h2>
    <svg class="divider" width="190" height="20" viewBox="0 0 190 20"><line x1="0" y1="10" x2="78" y2="10" stroke="#fff" stroke-width="2"/><line x1="112" y1="10" x2="190" y2="10" stroke="#fff" stroke-width="2"/><circle cx="95" cy="10" r="7" fill="none" stroke="#fff" stroke-width="2"/></svg></div>
  <article class="b-card" style="left:99px"><div class="b-photo" role="img" aria-label="Man checking a receding hairline in a mirror" style="background:linear-gradient(135deg,#d8d8d8,#8c7a6e)"></div><h3>Nemo enim ipsam voluptatem</h3><p>Nemo enim ipsam voluptatem quia voluptas sit aspernatur aut odit aut fugit, sed quia consequuntur magni dolores.</p><span class="btn">Read More</span></article>
  <article class="b-card" style="left:455px"><div class="b-photo" role="img" aria-label="Doctor inspecting the scalp of a patient" style="background:linear-gradient(135deg,#e6e2de,#a88a76)"></div><h3>Nemo enim ipsam voluptatem</h3><p>Nemo enim ipsam voluptatem quia voluptas sit aspernatur aut odit aut fugit, sed quia consequuntur magni dolores.</p><span class="btn">Read More</span></article>
  <article class="b-card" style="left:810px"><div class="b-photo" role="img" aria-label="Man with thinning hair holding his head" style="background:linear-gradient(135deg,#c7b0a2,#eee6df)"></div><h3>Nemo enim ipsam voluptatem</h3><p>Nemo enim ipsam voluptatem quia voluptas sit aspernatur aut odit aut fugit, sed quia consequuntur magni dolores.</p><span class="btn">Read More</span></article>
</section>

<footer>©2016 Hanbit Hair Clinic, All Right Reserved</footer>

</body>
</html>
```